Newsletter Ad

I am looking for someone to design an advertisement for a mother's club newsletter. 4" wide X by 5" tall (and 2.5" wide X 5" tall if possible).

I'm a psychotherapist, so want the ad to look professional, but modern. I have a logo with my photo attached that can be incorporated into the design. The colors of my website are turquoise and white. I'd like to keep with that theme...so maybe some turquoise blocking to match the logo font color.

I'm uploading a logo as well as an ad draft with the content I'd like listed in the ad.

```html
<!DOCTYPE html>
<html lang="en">
<head>
<meta charset="utf-8">
<title>Dana Whitlow – Psychotherapy Newsletter Ad</title>
<link rel="stylesheet" href="https://fonts.googleapis.com/css2?family=Roboto+Condensed:wght@300;400;700&family=Montserrat:wght@300;400&display=swap">
<style>
  :root {
    --teal: #4fa3a3;
    --white: #ffffff;
    --ink: #2c2c2c;
    --leaf-dark: #2f6a22;
    --leaf: #4e9a32;
    --leaf-light: #6fb34c;
    --portrait-dark: #1c1714;
    --portrait-warm: #5a4536;
  }
  * { margin: 0; padding: 0; box-sizing: border-box; }
  html, body { width: 960px; height: 1200px; overflow: hidden; background: var(--teal); }
  .ad {
    position: relative;
    width: 960px;
    height: 1200px;
    background: var(--teal);
    font-family: "Roboto Condensed", "Arial Narrow", sans-serif;
    color: var(--ink);
  }
  .hero {
    position: absolute;
    left: 36px; top: 36px;
    width: 888px; height: 538px;
    background: linear-gradient(180deg, var(--leaf-dark) 0%, var(--leaf) 50%, var(--leaf-light) 100%);
  }
  .headline-band {
    position: absolute;
    left: 36px; top: 574px;
    width: 888px; height: 66px;
    display: flex; align-items: center; justify-content: center;
    color: var(--white);
    font-weight: 700;
    font-size: 40.5px;
    white-space: nowrap;
  }
  .panel {
    position: absolute;
    left: 36px; top: 640px;
    width: 888px; height: 524px;
    background: var(--white);
  }
  .services {
    position: absolute;
    left: 0; top: 22px;
    width: 888px;
    list-style: none;
    font-weight: 300;
    font-size: 37px;
    line-height: 48px;
    text-align: center;
  }
  .services li { display: inline-block; margin: 0 12px; }
  .services li::before {
    content: "";
    display: inline-block;
    width: 13px; height: 13px;
    background: var(--ink);
    transform: rotate(45deg);
    margin-right: 28px;
    vertical-align: 6px;
  }
  .portrait {
    position: absolute;
    left: 17px; top: 213px;
    width: 290px; height: 295px;
    background: linear-gradient(180deg, var(--portrait-dark) 0%, var(--portrait-warm) 100%);
  }
  .brand {
    position: absolute;
    left: 322px; top: 440px;
    text-align: right;
    color: var(--teal);
    font-family: "Montserrat", sans-serif;
    font-weight: 400;
    line-height: 1;
  }
  .brand-name { font-size: 33px; letter-spacing: 0.5px; }
  .brand-credentials { font-size: 19px; letter-spacing: 1px; margin-top: 8px; }
  .contact {
    position: absolute;
    right: 16px; top: 274px;
    text-align: right;
    font-style: normal;
    font-weight: 300;
    font-size: 29px;
    line-height: 35px;
  }
  .contact .phone { font-weight: 700; }
  .license {
    position: absolute;
    right: 16px; top: 486px;
    font-weight: 300;
    font-size: 22px;
  }
</style>
</head>
<body>
<main class="ad">
  <div class="hero" role="img" aria-label="Photograph of a hand touching a white water lily among green lily pads"></div>

  <h1 class="headline-band">Psychotherapy for Individuals, Couples and Families</h1>

  <section class="panel">
    <ul class="services">
      <li>Parenting</li><li>Depression</li><li>Anxiety</li><li>Life Transitions</li><br>
      <li>Divorce</li><li>Couples Issues</li><li>Women’s Issues</li><br>
      <li>Attachment and Neuroscience</li>
    </ul>

    <div class="portrait" role="img" aria-label="Portrait photograph of the therapist"></div>

    <div class="brand">
      <div class="brand-name">DANA WHITLOW</div>
      <div class="brand-credentials">MA, MFT</div>
    </div>

    <address class="contact">
      418 Alder Lane<br>
      Fairbrook, CA 94900<br>
      www.danawhitlow.com<br>
      dana@danawhitlow.com<br>
      <span class="phone">415 555 0187</span>
    </address>

    <div class="license">License# MFC48203</div>
  </section>
</main>
</body>
</html>
```